Automotive debt collection business need several banners for new website

We are a debt recovery company called Quellton Recoveries Ltd who work specifically within the car automotive industry acting on behalf of our clients to recover debt which is owed to them. The advantage to using a company such as QRL is that it allows our clients the ability to outsource the work, removing the headache of dealing with the general public and reduces internal staff/overhead costs.
We collect various types of debt including:
Excess Mileage - this is charged when an individual has exceeded their permitted mileage allowance. This is calculated on a pence per mile basis on the mileage over the limit set when the contract was signed.
Damage - charged when a vehicle sustains more damage than is permitted within the contract. Damage could be dents to bodywork, large scratches, torn seats etc. Every area of damage over and above the allowed levels is detailed via a 'Damage Report' and a cost associated to that area of damage. The individual costs are then added up and a total charge formulated. The customer is liable to pay these charges as they have not cared for the vehicle in the appropriate manner whilst under their control
End of Contract Arrears - Once a contract ends and a vehicle is returned to our clients, there may be other charges that need to be repaid that remain outstanding.
We collect debt using a simple process. 1 - The customer is sent a letter as soon as the vehicle is collected advising them of the value of the debt. 2 - A few days later, we attempt to make contact via telephone or email. 3 - Once we contact the customer, we explain the debt and how the figure has been formulated (which is also explain in their letters). 4 - We negotiate (where appropriate) and agree a settlement figure. 5 - The customer pays the debt either in one installment over over a short payment plan.
Our new website (test URL only - http://testing.quelltonrecoveries.co.uk/) has a dual purpose. Firstly its to help promote our services to new clients who may be in the market for an alternative supplier (as far as we are aware, we are the only dedicated automotive debt collection company in the UK) and secondly, as a site to help those who owe money to pay and understand who we are (and that we are a registered, legal debt collection company)
Unlike other debt collection websites, we do not want generic images of people shaking hands, smiling etc. We want the images to be visually striking and make the website stand out from the competition. We are happy for these to be graphics rather than images.
We require some visual banners to represent what we do as a business and to emphasis that we specifically collect debt for the automotive sector.
These are websites that contain banners that we are NOT looking for:
http://uk.vabrix-partners.com/consumers/contact-data-working-hours/ - bland images of call centers/random people on phones etc
http://www.almsfield.com/client/
These are websites that contain banners that we class as OK:
http://www.norvanta.co.uk/business-services/debt-collection.html - fairly clear way of explaining their services
http://www.estatedues.co.uk/ - a slightly different slant using non-related images to explain what they can and cant do
http://www.pkwholdings.com/home/#.UhNNeD98CL0 - uses text to text banners to explain their offering
We require:
x4 - 870px X 500px - these will appear on the main homepage and rotate
x2 - 270px X 240px - static images that will to the right of the home page. One image needs to indicate some type of payment method as its a link to our online payment system, the second image refers to our other services (see the appropriate page on the website) these additional services include asset recovery, inspection, bespoke software solutions for the asset industry and auction disposal
x3 - 90px X 90px - Static images to represent payment methods that include cheque/card/bank transfer (see website for more info)
Our corporate colours are Black/Red/Grey
Depending on the designs received, we expect 2 rounds of modifications and we will advise those designers that have not been successful with positive feedback. We guarantee to pay the successful designer but work must be completed and ALL requested material produced and approved.

```html
<!DOCTYPE html>
<html lang="en">
<head>
<meta charset="utf-8">
<title>Quellton Recoveries Ltd</title>
<link rel="stylesheet" href="https://fonts.googleapis.com/css2?family=Arimo:wght@400;700&family=Jost:wght@400;500&family=Pathway+Gothic+One&family=Open+Sans:wght@700&display=swap">
<style>
  :root {
    --page-bg: #ffffff;
    --rule: #000000;
    --frame-shadow: #e6e6e6;
    --ink: #222222;
    --brand-red: #c41e24;
    --deep-red: #7a0f17;
    --portal-grey: #a0a9b3;
    --nav-grey: #676a73;
    --nav-tab: #595c64;
    --banner-bg: #e4e5e7;
    --panel-grey: #7f8891;
    --sub-ink: #4a4a4a;
    --white: #ffffff;
  }
  * { margin: 0; padding: 0; box-sizing: border-box; }
  html, body {
    width: 1200px; height: 654px; overflow: hidden;
    background: var(--page-bg);
    font-family: "Arimo", Arial, sans-serif;
  }
  .canvas {
    position: relative; width: 1200px; height: 654px;
    border-top: 1px solid var(--rule);
  }
  .sheet {
    position: absolute; left: 92px; top: 0; width: 1020px; height: 654px;
    background: var(--page-bg);
    box-shadow: -2px 0 3px var(--frame-shadow), 2px 0 3px var(--frame-shadow);
  }
  .brand {
    position: absolute; left: 114px; top: 44px;
    font-family: "Jost", sans-serif; font-weight: 500;
    font-size: 40px; letter-spacing: 2px; color: var(--ink);
    display: flex; align-items: center; gap: 10px;
  }
  .brand-dot { width: 14px; height: 14px; border-radius: 50%; background: var(--brand-red); }
  .portal-box {
    position: absolute; left: 840px; top: 18px; width: 255px; height: 93px;
    background: var(--portal-grey); border: 1px solid var(--deep-red);
    padding: 27px 0 0 17px; color: var(--deep-red);
  }
  .portal-title { font-weight: 700; font-size: 15.5px; }
  .portal-note { font-size: 12px; margin-top: 11px; }
  .main-nav {
    position: absolute; left: 109px; top: 137px; width: 986px; height: 50px;
    background: var(--nav-grey);
  }
  .nav-tab {
    position: absolute; left: 0; top: 0; width: 32px; height: 50px;
    background: var(--nav-tab); color: var(--white); font-size: 11px;
    padding: 7px 0 0 6px;
  }
  .nav-link {
    position: absolute; top: 18px; color: var(--white); font-size: 12px;
    text-decoration: none; white-space: nowrap;
  }
  .hero-banner {
    position: absolute; left: 109px; top: 212px; width: 733px; height: 422px;
    background: var(--banner-bg); overflow: hidden;
  }
  .banner-title {
    position: absolute; left: 38px; top: 18px;
    font-family: "Jost", sans-serif; font-weight: 500;
    font-size: 58px; line-height: 54px; letter-spacing: 1.5px;
    color: var(--brand-red);
  }
  .banner-sub {
    position: absolute; left: 37px; top: 148px;
    font-family: "Pathway Gothic One", sans-serif;
    font-size: 24px; line-height: 28px; color: var(--sub-ink);
  }
  .vehicle-art {
    position: absolute; left: 253px; top: 53px; width: 464px; height: 346px;
  }
  .promo-panel {
    position: absolute; left: 842px; top: 212px; width: 253px; height: 422px;
    background: var(--panel-grey); color: var(--white);
    padding: 26px 24px 0 25px;
  }
  .promo-heading { font-size: 19.5px; line-height: 23px; font-weight: 400; }
  .promo-heading strong { font-weight: 700; display: block; }
  .promo-copy { font-size: 12px; line-height: 17.7px; margin-top: 17px; }
  .all-posts {
    position: absolute; left: 25px; top: 313px; width: 105px; height: 34px;
    background: var(--deep-red); color: var(--white);
    font-family: "Open Sans", sans-serif; font-weight: 700; font-size: 10px;
    display: flex; align-items: center; padding-left: 16px; gap: 9px;
    text-decoration: none;
  }
  .slide-controls { position: absolute; left: 168px; top: 371px; display: flex; gap: 8px; }
  .slide-button {
    width: 26px; height: 25px; background: var(--deep-red);
    display: flex; align-items: center; justify-content: center;
  }
</style>
</head>
<body>
<div class="canvas">
  <div class="sheet"></div>

  <div class="brand"><span>QRL</span><span class="brand-dot"></span></div>

  <aside class="portal-box">
    <h2 class="portal-title">Customer Portal</h2>
    <p class="portal-note">Our customer portal is comming soon</p>
  </aside>

  <nav class="main-nav">
    <span class="nav-tab">~</span>
    <a class="nav-link" style="left:53px">About Us</a>
    <a class="nav-link" style="left:143px">Features</a>
    <a class="nav-link" style="left:233px">Additional Services</a>
    <a class="nav-link" style="left:376px">FAQ</a>
    <a class="nav-link" style="left:442px">Payment Portal</a>
    <a class="nav-link" style="left:568px">Contact Us</a>
  </nav>

  <section class="hero-banner">
    <h1 class="banner-title">Damage<br>Report</h1>
    <p class="banner-sub">Charged when a vehicle sustains<br>more damage than is permitted<br>within the contract</p>
    <svg class="vehicle-art" role="img" aria-label="Photo of a damaged red hatchback with open doors and bonnet" viewBox="0 0 464 346">
      <defs>
        <radialGradient id="carTone" cx="55%" cy="50%" r="60%">
          <stop offset="0" stop-color="#d42a2e"/>
          <stop offset="0.7" stop-color="#b51d22" stop-opacity="0.85"/>
          <stop offset="1" stop-color="#e4e5e7" stop-opacity="0"/>
        </radialGradient>
      </defs>
      <rect width="464" height="346" rx="40" fill="url(#carTone)"/>
    </svg>
  </section>

  <aside class="promo-panel">
    <h2 class="promo-heading">HAPPY<br>CUSTOMERS<strong>BUY NOW</strong></h2>
    <p class="promo-copy">Mauris gravida vulputate ligula, ut sagittis libero consequat nec. Morbi mi sapien, viverra non interdum rutrum, viverra et massa. Suspendisse potenti. Vivamus orci nibh, egestas ac adipiscing id, tempus in justo. Duis blandit volutpat nunc nec dictum. Sed eget lectus sed est condimentum ultricies ut quis nunc. Aliquam mollis interdum condimentum.</p>
    <a class="all-posts">ALL POSTS
      <svg width="9" height="9" viewBox="0 0 9 9"><path d="M2 1l4 3.5L2 8" fill="none" stroke="#fff" stroke-width="1.4"/></svg>
    </a>
    <div class="slide-controls">
      <span class="slide-button"><svg width="10" height="10" viewBox="0 0 10 10"><path d="M7 1L3 5l4 4" fill="none" stroke="#fff" stroke-width="1.6"/></svg></span>
      <span class="slide-button"><svg width="10" height="10" viewBox="0 0 10 10"><path d="M3 1l4 4-4 4" fill="none" stroke="#fff" stroke-width="1.6"/></svg></span>
    </div>
  </aside>
</div>
</body>
</html>
```